Innovative Web Application Welcome Page with Free Trial and Embedded Video

We run the Kestrel Response Orchestration Suite (https://kestrel.vantorisdefense.example), which is the world's first security automation cloud that delivers automated security to organisations.Our existing Welcome page (page shown after login) needs redesigning to be inline with our new Kestrel brand (i.e. the Kestrel website - innovative and global). The Welcome Page will promote a 30-day trial of our Proactive Breached Login Surveillance feature. Screenshots attached including current Welcome Page, mock up of new Welcome Page content, Kestrel logos, Kestrel brochures, Kestrel main brand hero image, slide images, etc. The application header and side menu must remain the same. The design is for the main section of this page.

Target Market(s)

IT Security

Number of Pages Required

1 page

Font styles to use
Sans Serif
Other font styles liked:
• Website creative specifications sheet attached

Colors

Designer to choose only greyscale colors for use in the design.

Requirements
Must have
• All sections and text in the mockup image provided

```html
<!DOCTYPE html>
<html lang="en">
<head>
<meta charset="utf-8">
<title>Kestrel – Welcome</title>
<link rel="stylesheet" href="https://fonts.googleapis.com/css2?family=Mulish:wght@300;400;800&family=Rubik:wght@500;700&family=Roboto:wght@400&display=swap">
<style>
  :root{
    --topbar:#222a31;
    --sidebar:#2d3640;
    --sidebar-deep:#262e36;
    --menu-text:#c9ced3;
    --menu-icon:#aab1b8;
    --red:#e3262a;
    --white:#ffffff;
    --ink:#222222;
    --body:#3a3a3a;
    --button:#2a323a;
    --footer:#1f2428;
    --black:#050505;
  }
  *{box-sizing:border-box;margin:0;padding:0}
  html,body{width:1200px;height:1011px;overflow:hidden;background:var(--white)}
  body{position:relative;font-family:"Mulish",sans-serif}

  .topbar{position:absolute;left:0;top:0;width:1200px;height:42px;background:var(--topbar)}
  .topbar .tag{position:absolute;top:17px;left:1086px;font:400 4px "Roboto",sans-serif;color:#6d757c;letter-spacing:.3px}
  .topbar .menu{position:absolute;top:14px;font:400 10px "Roboto",sans-serif;color:#c9ced3}
  .topbar .menu::after{content:"";display:inline-block;margin-left:4px;border:3.5px solid transparent;border-top:4px solid #c9ced3;vertical-align:-1px}

  .sidebar{position:absolute;left:0;top:0;width:176px;height:1011px;background:var(--sidebar)}
  .sidebar .brand{height:64px;background:var(--topbar);padding:21px 0 0 18px;font:300 34px "Mulish",sans-serif;color:var(--white);line-height:1}
  .profile{position:relative;height:84px;background:radial-gradient(ellipse at 60% 50%,#5b6771 0%,#39434c 55%,#2b333b 100%)}
  .profile .tag{position:absolute;left:16px;top:28px;font:400 4px "Roboto",sans-serif;color:#8a939b;letter-spacing:.3px}
  .profile .user{position:absolute;left:14px;top:54px;font:400 11px "Roboto",sans-serif;color:var(--white)}
  .nav{list-style:none;margin-top:5px}
  .nav li{position:relative;height:27.2px;display:flex;align-items:center;padding-left:14px;font:400 9.5px "Roboto",sans-serif;color:var(--menu-text)}
  .nav li svg{width:12px;height:12px;margin-right:8px;fill:var(--menu-icon)}
  .nav li.has-sub::after{content:"";position:absolute;left:146px;top:11px;width:4px;height:4px;border-right:1.2px solid #8b939a;border-top:1.2px solid #8b939a;transform:rotate(45deg)}
  .collapse{position:absolute;left:139px;top:511px;width:37px;height:23px;background:var(--sidebar-deep);border-radius:12px 0 0 12px;color:var(--white);font:700 13px "Roboto",sans-serif;text-align:center;line-height:22px}

  .hero{position:absolute;left:176px;top:42px;width:1024px;height:476px;overflow:hidden;
    background:radial-gradient(ellipse at 68% 45%,#8a8a8a 0%,#555 35%,#2c2c2c 75%,#1a1a1a 100%)}
  .hero .photo{position:absolute;inset:0}
  .hero .logo{position:absolute;left:40px;top:38px;font:300 56px "Mulish",sans-serif;color:var(--white);line-height:1}
  .headline{position:absolute;left:560px;top:90px;width:416px;text-align:center;font:700 29px/43.5px "Rubik",sans-serif;color:var(--white);text-transform:uppercase}
  .headline .accent{color:var(--red)}
  .cta{position:absolute;left:674px;top:274px;width:186px;height:42px;background:var(--button);border-radius:3px;color:var(--white);font:500 16px/42px "Rubik",sans-serif;text-align:center}

  .welcome{position:absolute;left:176px;top:518px;width:1024px;height:356px}
  .welcome h1{position:absolute;left:43px;top:47px;font:300 38px "Mulish",sans-serif;color:var(--ink);white-space:nowrap}
  .welcome h1 strong{font-weight:800}
  .welcome p{position:absolute;left:43px;top:109px;width:460px;font:400 16px/30.4px "Mulish",sans-serif;color:var(--body)}
  .video{position:absolute;left:558px;top:47px;width:422px;height:259px;border:2px solid var(--red);padding:4px}
  .video svg{display:block}

  .footer{position:absolute;left:176px;top:874px;width:1024px;height:137px;background:var(--footer)}
  .footer .legal{position:absolute;top:35px;width:100%;text-align:center;font:400 14.5px "Mulish",sans-serif;color:var(--white)}
  .social{position:absolute;top:72px;left:425px;display:flex;gap:6px}
  .social span{width:30px;height:30px;border:1.2px solid var(--white);border-radius:50%}
  .footer .build{position:absolute;right:18px;top:104px;font:400 11px "Roboto",sans-serif;color:#ddd}
</style>
</head>
<body>

<header class="topbar">
  <span class="tag">ALERT</span>
  <span class="menu" style="left:1118px">Ty</span>
  <span class="menu" style="left:1162px">US</span>
</header>

<aside class="sidebar">
  <div class="brand">Kestrel</div>
  <div class="profile" role="img" aria-label="Profile banner photo of two antelopes in dust">
    <span class="tag">ALERT</span>
    <span class="user">Ty</span>
  </div>
  <ul class="nav">
    <li class="has-sub"><svg viewBox="0 0 12 12"><circle cx="4.5" cy="6" r="3.5"/><circle cx="9.5" cy="3" r="2"/></svg>Automation</li>
    <li class="has-sub"><svg viewBox="0 0 12 12"><path d="M1 4h10l-1.5 7h-7z"/></svg>Marketplace</li>
    <li class="has-sub"><svg viewBox="0 0 12 12"><circle cx="3" cy="8" r="2.5"/><circle cx="8" cy="4" r="2.5"/><circle cx="9" cy="9.5" r="2"/></svg>Workflows</li>
    <li class="has-sub"><svg viewBox="0 0 12 12"><path d="M6 1l5 2.5v5L6 11 1 8.5v-5z"/></svg>Modules</li>
    <li class="has-sub"><svg viewBox="0 0 12 12"><rect x="0" y="1" width="4" height="3"/><rect x="8" y="1" width="4" height="3"/><rect x="4" y="8" width="4" height="3"/></svg>Services</li>
    <li><svg viewBox="0 0 12 12"><path d="M0 2h5l1 1.5h6V11H0z"/></svg>Containers</li>
    <li><svg viewBox="0 0 12 12"><rect x="0" y="1" width="5" height="4.5"/><rect x="7" y="1" width="5" height="4.5"/><rect x="0" y="7" width="5" height="4.5"/><rect x="7" y="7" width="5" height="4.5"/></svg>Dashboards</li>
    <li class="has-sub"><svg viewBox="0 0 12 12"><path d="M0 1h1.2v9.8H12V12H0z"/><path d="M2 9l3-4 2.5 2L11 3" stroke="#aab1b8" stroke-width="1.3" fill="none"/></svg>Charts</li>
    <li><svg viewBox="0 0 12 12"><circle cx="6" cy="3" r="2.5"/><path d="M1 12c0-4 2-5.5 5-5.5s5 1.5 5 5.5z"/></svg>Agents</li>
    <li class="has-sub"><svg viewBox="0 0 12 12"><rect x="1.5" y="5" width="9" height="7"/><path d="M3.5 5V3.5a2.5 2.5 0 015 0V5" stroke="#aab1b8" stroke-width="1.4" fill="none"/></svg>Credentials</li>
    <li class="has-sub"><svg viewBox="0 0 12 12"><rect x="1.5" y="5" width="9" height="7"/><path d="M3.5 5V3.5a2.5 2.5 0 015 0V5" stroke="#aab1b8" stroke-width="1.4" fill="none"/></svg>Security Zones</li>
    <li><svg viewBox="0 0 12 12"><rect x="1" y="2" width="10" height="10"/><rect x="3" y="0" width="1.4" height="3"/><rect x="7.6" y="0" width="1.4" height="3"/></svg>Events</li>
    <li><svg viewBox="0 0 12 12"><circle cx="4.5" cy="3" r="2.5"/><path d="M0 11c0-3.5 2-5 4.5-5s4.5 1.5 4.5 5z"/><circle cx="10" cy="9" r="2"/></svg>Security Services</li>
  </ul>
  <div class="collapse">«</div>
</aside>

<section class="hero">
  <svg class="photo" width="1024" height="476" role="img" aria-label="Hero photograph of two oryx clashing horns in dust, left half tinted red">
    <defs>
      <linearGradient id="redTint" x1="0" y1="0" x2="0" y2="1">
        <stop offset="0" stop-color="#6a0b0d"/>
        <stop offset="0.35" stop-color="#e02428"/>
        <stop offset="0.85" stop-color="#b81a1e"/>
        <stop offset="1" stop-color="#5a0a0c"/>
      </linearGradient>
      <linearGradient id="ground" x1="0" y1="0" x2="0" y2="1">
        <stop offset="0" stop-color="#000" stop-opacity="0"/>
        <stop offset="1" stop-color="#000" stop-opacity="0.55"/>
      </linearGradient>
    </defs>
    <path d="M0 0H370C470 80 560 220 545 300C530 400 500 450 470 476H0z" fill="url(#redTint)"/>
    <rect y="360" width="1024" height="116" fill="url(#ground)"/>
  </svg>
  <div class="logo">Kestrel</div>
  <h2 class="headline"><span class="accent">30-Day Trial</span><br>of our Proactive<br><span class="accent">Breached Login</span><br>Surveillance Feature</h2>
  <div class="cta">START FREE TRIAL</div>
</section>

<main class="welcome">
  <h1>Welcome to <strong>Kestrel</strong></h1>
  <p>Sed ut perspiciatis unde omnis iste natus error sit voluptatem acantium doloremque laudantium, totam rem aperiam, eaque ipsa quae ab illo inventore veritatis et quasi architecto beatae vitae dicta sunt explicabo. Nemo enim ipsam voluptatem quia voluptas sit aspernatur aut odit aut fugit, sed quia conseq uuntur magni dolores eos voluptatem quia</p>
  <div class="video">
    <svg width="410" height="247" viewBox="0 0 410 247" aria-label="Getting started video">
      <rect width="410" height="247" fill="var(--black)"/>
      <path d="M0 0H134L232 247H0z" fill="var(--red)"/>
      <circle cx="356" cy="50" r="20" fill="none" stroke="#fff" stroke-width="3"/>
      <path d="M350 40v20l15-10z" fill="#fff"/>
      <g font-family="Mulish, sans-serif" font-weight="300" fill="#fff" font-size="18" text-anchor="end">
        <text x="150" y="127">GETTING</text>
        <text x="150" y="144">STARTED</text>
        <text x="150" y="161">WITH</text>
      </g>
      <text x="162" y="160" font-family="Mulish, sans-serif" font-weight="300" font-size="62" fill="#fff">Kestrel</text>
      <text x="213" y="178" font-family="Mulish, sans-serif" font-weight="400" font-size="11" letter-spacing="1" fill="#fff">SECURITY AUTOMATION</text>
    </svg>
  </div>
</main>

<footer class="footer">
  <div class="legal">© 2019 Kestrel. All Rights Reserved | Privacy Policy | Terms and Conditions</div>
  <div class="social">
    <span aria-label="Social link"></span>
    <span aria-label="Social link"></span>
    <span aria-label="Social link"></span>
    <span aria-label="Social link"></span>
    <span aria-label="Social link"></span>
  </div>
  <div class="build">c7</div>
</footer>

</body>
</html>
```